Security Warning Sign

We have an existing sign that needs an update. I have attached a picture of the current square sign. We need to maintain the same wording. It needs to be professional and appropriate to attach to our customers fence. Also attached is a copy of our building sign which may lend some inspiration and hopefully the ai format will assist. The final sign will be 600mm x 600mmOur website is www.halvorngate.com.au

```html
<!DOCTYPE html>
<html lang="en">
<head>
<meta charset="utf-8">
<title>Halvorn Gate Security – Surveillance Warning Sign</title>
<link rel="stylesheet" href="https://fonts.googleapis.com/css2?family=Anton&family=Roboto+Condensed:wght@700&display=swap">
<style>
  :root {
    --sign-white: #ffffff;
    --ink-black: #111111;
    --band-black: #141414;
    --warn-orange: #f7911e;
    --warn-red: #ff1500;
  }
  html, body {
    margin: 0;
    padding: 0;
    width: 1200px;
    height: 1200px;
    overflow: hidden;
    background: var(--sign-white);
  }
  .sign {
    position: relative;
    width: 1200px;
    height: 1200px;
    background: var(--sign-white);
  }
  .sign-art {
    position: absolute;
    inset: 0;
    width: 1200px;
    height: 1200px;
    display: block;
  }
  .headline {
    font-family: "Anton", "Impact", sans-serif;
    fill: var(--ink-black);
  }
  .notice-line {
    font-family: "Roboto Condensed", "Arial Narrow", sans-serif;
    font-weight: 700;
    fill: var(--ink-black);
  }
  .brand-name {
    font-family: "Roboto Condensed", "Arial Narrow", sans-serif;
    font-weight: 700;
    fill: var(--sign-white);
  }
  .phone-number {
    font-family: "Roboto Condensed", "Arial Narrow", sans-serif;
    font-weight: 700;
    fill: var(--sign-white);
  }
</style>
</head>
<body>
<main class="sign">
  <svg class="sign-art" viewBox="0 0 1200 1200" xmlns="http://www.w3.org/2000/svg">
    <defs>
      <clipPath id="warning-panel-clip">
        <polygon points="100,118 600,62 1100,118 1122,260 1100,402 600,452 100,402 78,260"/>
      </clipPath>
    </defs>

    <!-- Warning panel -->
    <g class="warning-panel">
      <polygon points="88,106 600,46 1112,106 1136,260 1112,414 600,468 88,414 64,260"
               fill="none" stroke="var(--warn-orange)" stroke-width="5"/>
      <g clip-path="url(#warning-panel-clip)">
        <rect x="60" y="40" width="540" height="440" fill="var(--warn-orange)"/>
        <rect x="600" y="40" width="560" height="440" fill="var(--warn-red)"/>
      </g>
      <text class="headline" x="600" y="340" text-anchor="middle"
            font-size="238" textLength="890" lengthAdjust="spacingAndGlyphs">WARNING!</text>
    </g>

    <!-- Notice text -->
    <g class="notice">
      <text class="notice-line" x="600" y="610" text-anchor="middle"
            font-size="92" textLength="1084" lengthAdjust="spacingAndGlyphs">ELECTRONIC SURVEILLANCE</text>
      <text class="notice-line" x="600" y="724" text-anchor="middle"
            font-size="92" textLength="966" lengthAdjust="spacingAndGlyphs">AND RECORDING DEVICES</text>
      <text class="notice-line" x="600" y="838" text-anchor="middle"
            font-size="92" textLength="960" lengthAdjust="spacingAndGlyphs">INSTALLED IN THIS AREA</text>
    </g>

    <!-- Footer band -->
    <g class="footer-band">
      <rect x="0" y="963" width="1200" height="237" fill="var(--band-black)"/>
      <polygon points="612,990 1200,963 1200,1012" fill="var(--warn-orange)"/>
      <polygon points="0,963 612,963 612,990 0,990" fill="var(--band-black)"/>
    </g>

    <!-- Company name -->
    <g class="brand">
      <circle cx="150" cy="1084" r="60" fill="var(--warn-orange)"/>
      <text class="brand-name" x="236" y="1058" font-size="46">HALVORN</text>
      <text class="brand-name" x="236" y="1104" font-size="46">GATE</text>
      <text class="brand-name" x="236" y="1150" font-size="46">SECURITY</text>
    </g>

    <!-- Phone -->
    <g class="contact">
      <rect x="684" y="1071" width="50" height="50" rx="6" fill="var(--warn-orange)"/>
      <path d="M699 1081 c-4 0 -6 4 -5 9 c2 10 9 19 19 23 c5 2 9 0 10 -4 l1 -3 c0 -2 -1 -3 -3 -4 l-6 -2 c-2 -1 -3 0 -4 1 l-2 3 c-5 -2 -9 -6 -11 -11 l3 -2 c1 -1 2 -2 1 -4 l-2 -6 c-1 -2 -2 -2 -4 -2 z"
            fill="var(--band-black)"/>
      <text class="phone-number" x="748" y="1118" font-size="66"
            textLength="395" lengthAdjust="spacingAndGlyphs">1300 555 014</text>
    </g>
  </svg>
</main>
</body>
</html>
```